Marlowick APP redesign and color change

I am looking for a new design for my app. Please see the attached current design.

Currently, I have a functioning app but the colors and design are awful!
The logo is great but the rest of the app needs a refresh.
(Logo hi res not yet available but will upload soon.)
New colors or anything that is cutting edge.

Basically: It is a secure social media app within a school system where the teachers, students and parents can text, exchange photos, plan curriculum, etc.

I NEED ONLY landing page with a new look!
Looking for one distinct design for the landing page with new look.
The developer will apply this one design towards the rest of the pages/app screens.

Because part of the social media I need the feel and look of what is now the trend. Something that will attract and keep the client(s) interested. I am really leaving all the creative work to the designer and open to any suggestions.
Updates

Target Market(s)

Schools, community, teachers, students, colleges, sport teams

Industry/Entity Type

Non Profit

Font styles to use
Serif
Sans Serif

Colors

Designer to choose colors to be used in the design.

Requirements
Must have
• Sharp, trendy, millennial feel
Nice to have
• Up to designer
Should not have
• Up to designer

```html
<!DOCTYPE html>
<html lang="en">
<head>
<meta charset="utf-8">
<title>Marlowick – Sign in</title>
<link href="https://fonts.googleapis.com/css2?family=Roboto:wght@400;500;700&display=swap" rel="stylesheet">
<style>
  :root {
    --page-bg: #111111;
    --screen-bg: #eceff2;
    --ink: #2b2b2b;
    --ink-soft: #555a60;
    --muted: #8a8f94;
    --field-bg: #ffffff;
    --field-focus: #a9c6ee;
    --link-blue: #1a4fd6;
    --green: #22b043;
    --violet: #7a5bf4;
    --white: #ffffff;
  }
  * { box-sizing: border-box; margin: 0; padding: 0; }
  html, body { width: 1200px; height: 1200px; overflow: hidden; }
  body {
    background: var(--page-bg);
    font-family: "Roboto", sans-serif;
    position: relative;
  }
  .screen {
    position: absolute;
    left: 287px; top: 42px;
    width: 626px; height: 1116px;
    background: var(--screen-bg);
    overflow: hidden;
  }
  .status-bar {
    position: absolute; left: 0; top: 8px; width: 100%; height: 30px;
    display: flex; align-items: center; justify-content: space-between;
    padding: 0 14px; font-size: 18px; color: var(--ink);
  }
  .status-left, .status-right { display: flex; align-items: center; gap: 6px; }
  .status-time { position: absolute; left: 0; right: 0; text-align: center; }
  .brand {
    position: absolute; left: 0; top: 326px; width: 100%; text-align: center;
    color: var(--ink);
  }
  .brand-name {
    font-weight: 700; font-size: 27px; letter-spacing: 0.5em;
    padding-left: 0.5em; line-height: 1;
  }
  .brand-tagline {
    margin-top: 14px; font-size: 14px; letter-spacing: 0.07em; font-weight: 400;
  }
  .field {
    position: absolute; left: 42px; width: 542px;
    background: var(--field-bg);
    display: flex; align-items: center; justify-content: space-between;
    padding: 0 16px; font-size: 22px;
  }
  .field-email { top: 481px; height: 58px; border: 1.5px solid var(--field-focus); color: var(--link-blue); }
  .field-email .caret { display: inline-block; width: 1px; height: 28px; background: var(--ink-soft); margin-left: 6px; vertical-align: middle; }
  .field-password { top: 547px; height: 56px; color: var(--muted); }
  .options {
    position: absolute; left: 42px; width: 542px; top: 622px; height: 28px;
    display: flex; align-items: center; justify-content: space-between; font-size: 18px;
  }
  .remember { display: flex; align-items: center; gap: 10px; color: var(--green); }
  .forgot { color: var(--muted); }
  .btn-login {
    position: absolute; left: 42px; top: 689px; width: 542px; height: 56px;
    background: var(--green); color: var(--white);
    display: flex; align-items: center; justify-content: center;
    font-size: 20px; font-weight: 500;
  }
  .hero-photo {
    position: absolute; left: 0; top: 745px; width: 100%; height: 303px;
    background: linear-gradient(180deg, #eef1f4 0%, #e6e2df 55%, #d9cfcb 100%);
  }
  .btn-signup {
    position: absolute; left: 0; top: 1048px; width: 100%; height: 68px;
    background: var(--violet); color: var(--white);
    display: flex; align-items: center; justify-content: center;
    font-size: 19px; font-weight: 500;
  }
</style>
</head>
<body>
  <main class="screen">
    <div class="status-bar">
      <div class="status-left">
        <svg width="56" height="12" viewBox="0 0 56 12" aria-hidden="true">
          <circle cx="6" cy="6" r="5" fill="#2b2b2b"/>
          <circle cx="17" cy="6" r="5" fill="#2b2b2b"/>
          <circle cx="28" cy="6" r="5" fill="#2b2b2b"/>
          <circle cx="39" cy="6" r="4.3" fill="none" stroke="#2b2b2b" stroke-width="1.2"/>
          <circle cx="50" cy="6" r="4.3" fill="none" stroke="#2b2b2b" stroke-width="1.2"/>
        </svg>
        <span>VELA</span>
        <svg width="20" height="16" viewBox="0 0 20 16" aria-hidden="true">
          <path d="M1 5a13 13 0 0 1 18 0" fill="none" stroke="#2b2b2b" stroke-width="2.2"/>
          <path d="M4.5 8.5a8 8 0 0 1 11 0" fill="none" stroke="#2b2b2b" stroke-width="2.2"/>
          <path d="M10 15l-3-3a4 4 0 0 1 6 0z" fill="#2b2b2b"/>
        </svg>
      </div>
      <span class="status-time">4:21 PM</span>
      <div class="status-right">
        <svg width="12" height="18" viewBox="0 0 12 18" aria-hidden="true">
          <path d="M2 5l8 8-4 4V1l4 4-8 8" fill="none" stroke="#777" stroke-width="1.3"/>
        </svg>
        <span>100%</span>
        <svg width="40" height="16" viewBox="0 0 40 16" aria-hidden="true">
          <rect x="1" y="1" width="34" height="14" rx="2.5" fill="none" stroke="#2b2b2b" stroke-width="1.3"/>
          <rect x="3" y="3" width="30" height="10" rx="1.2" fill="#2b2b2b"/>
          <rect x="36.5" y="5.5" width="2.5" height="5" rx="1" fill="#2b2b2b"/>
        </svg>
      </div>
    </div>

    <header class="brand">
      <div class="brand-name">MARLOWICK</div>
      <div class="brand-tagline">SAFE SPACES FOR OPEN LEARNING</div>
    </header>

    <div class="field field-email">
      <span>dmorrow@<span class="caret"></span></span>
      <svg width="26" height="20" viewBox="0 0 26 20" aria-hidden="true">
        <rect x="0" y="0" width="26" height="20" rx="2" fill="#5b5f63"/>
        <path d="M1 2l12 9 12-9" fill="none" stroke="#ffffff" stroke-width="2"/>
      </svg>
    </div>

    <div class="field field-password">
      <span>Password</span>
      <svg width="22" height="28" viewBox="0 0 22 28" aria-hidden="true">
        <path d="M5 12V8a6 6 0 0 1 12 0v4" fill="none" stroke="#5b5f63" stroke-width="3"/>
        <rect x="0" y="12" width="22" height="16" rx="2" fill="#5b5f63"/>
        <rect x="9.5" y="17" width="3" height="6" rx="1.5" fill="#ffffff"/>
      </svg>
    </div>

    <div class="options">
      <div class="remember">
        <svg width="18" height="18" viewBox="0 0 18 18" aria-hidden="true">
          <rect x="1" y="1" width="16" height="16" rx="1.5" fill="none" stroke="#22b043" stroke-width="1.5"/>
          <path d="M4.5 9.5l3 3 6-7" fill="none" stroke="#22b043" stroke-width="1.6"/>
        </svg>
        <span>Remember me</span>
      </div>
      <span class="forgot">Forgot your password?</span>
    </div>

    <div class="btn-login">LOGIN</div>

    <div class="hero-photo" role="img" aria-label="Faded photo of a smiling schoolgirl raising one finger beside a stack of books topped with an apple"></div>

    <div class="btn-signup">SIGN UP FOR MARLOWICK</div>
  </main>
</body>
</html>
```